Timber Ridge Land Services Business Cards

Need to create a business card with the company logo "Timber Ridge Land Services". The business will provide forestry mulching for land clearing and vegetation control, brush and small tree removal, wildlife habitat improvement and trail and property access creation.

```html
<!DOCTYPE html>
<html lang="en">
<head>
<meta charset="utf-8">
<title>Timber Ridge Land Services – Business Cards</title>
<link href="https://fonts.googleapis.com/css2?family=Poppins:wght@300;400;600;700&display=swap" rel="stylesheet">
<style>
  :root {
    --backdrop: #9a9a9a;
    --forest: #005a4a;
    --forest-deep: #00483b;
    --forest-ink: #0a3d33;
    --leaf: #5cbf5e;
    --leaf-soft: #8fd68a;
    --paper: #ffffff;
    --ink: #2b2b2b;
  }
  * { box-sizing: border-box; margin: 0; padding: 0; }
  html, body {
    width: 1093px; height: 1200px; overflow: hidden;
    background: var(--backdrop);
    font-family: "Poppins", sans-serif;
  }
  .card {
    position: absolute;
    left: 264px;
    width: 580px;
    height: 358px;
    border-radius: 24px;
    overflow: hidden;
  }
  .card--front { top: 226px; background: var(--paper); }
  .card--back { top: 621px; background: var(--forest); }

  .name-marker {
    position: absolute; left: 0; top: 49px;
    width: 22px; height: 38px; background: var(--forest);
  }
  .holder { position: absolute; left: 32px; top: 45px; }
  .holder__name {
    font-weight: 700; font-size: 23px; line-height: 1.05;
    color: var(--forest); letter-spacing: 0.3px;
  }
  .holder__role {
    font-weight: 400; font-size: 17px; line-height: 1.1;
    color: var(--leaf); letter-spacing: 0.3px;
  }

  .brand {
    position: absolute; right: 26px; top: 70px;
    width: 250px; text-align: center;
    display: flex; flex-direction: column; align-items: center; gap: 8px;
  }
  .brand__mark { width: 14px; height: 14px; background: var(--leaf); }
  .brand__name {
    font-weight: 700; font-size: 25px; line-height: 1.15;
    color: var(--forest); text-transform: uppercase; letter-spacing: 0.5px;
  }

  .contact { position: absolute; left: 32px; top: 258px; list-style: none; }
  .contact__item {
    display: flex; align-items: center; gap: 7px;
    font-size: 17.5px; line-height: 21px; color: var(--ink);
  }
  .contact__icon { width: 15px; height: 15px; flex: none; }
  .contact__highlight { color: var(--leaf); }

  .address {
    position: absolute; right: 24px; top: 278px;
    text-align: right; font-size: 17.5px; line-height: 21px; color: var(--ink);
    font-style: normal;
  }

  .pattern-band {
    position: absolute; left: 0; right: 0; bottom: 0; height: 20px;
    background: linear-gradient(180deg, var(--leaf-soft) 0%, var(--leaf) 45%, var(--forest) 100%);
  }
  .card--back .pattern-band {
    height: 22px;
    background: linear-gradient(180deg, var(--leaf-soft) 0%, var(--leaf) 50%, var(--forest-deep) 100%);
  }

  .back-brand {
    position: absolute; left: 0; right: 0; top: 150px;
    display: flex; flex-direction: column; align-items: center; gap: 10px;
  }
  .back-brand .brand__mark { background: var(--forest-ink); width: 16px; height: 16px; }
  .back-brand__name {
    font-weight: 700; font-size: 32px; line-height: 1.15; text-align: center;
    color: var(--forest-ink); text-transform: uppercase; letter-spacing: 0.6px;
  }
</style>
</head>
<body>

<section class="card card--front">
  <div class="name-marker"></div>
  <div class="holder">
    <p class="holder__name">DANIEL HARTWELL</p>
    <p class="holder__role">Managing Director</p>
  </div>

  <div class="brand">
    <span class="brand__mark"></span>
    <p class="brand__name">Timber Ridge<br>Land Services</p>
  </div>

  <ul class="contact">
    <li class="contact__item">
      <svg class="contact__icon" viewBox="0 0 24 24"><path fill="#005a4a" d="M6.6 10.8a15.1 15.1 0 0 0 6.6 6.6l2.2-2.2a1 1 0 0 1 1-.25 11.4 11.4 0 0 0 3.6.57 1 1 0 0 1 1 1V20a1 1 0 0 1-1 1A17 17 0 0 1 3 4a1 1 0 0 1 1-1h3.5a1 1 0 0 1 1 1c0 1.250.2 2.45.57 3.57a1 1 0 0 1-.25 1z"/></svg>
      044-555 018 234
    </li>
    <li class="contact__item">
      <svg class="contact__icon" viewBox="0 0 24 24"><path fill="#005a4a" d="M2 5h20v14H2z"/><path fill="none" stroke="#fff" stroke-width="1.6" d="M2 5l10 8 10-8M2 19l7-7M22 19l-7-7"/></svg>
      info@timberridgeland.com
    </li>
    <li class="contact__item">
      <svg class="contact__icon" viewBox="0 0 24 24"><g fill="none" stroke="#005a4a" stroke-width="2"><circle cx="12" cy="12" r="10"/><ellipse cx="12" cy="12" rx="4.5" ry="10"/><path d="M2 12h20M4 7h16M4 17h16"/></g></svg>
      <span>www.<span class="contact__highlight">timberridgeland</span>.com</span>
    </li>
  </ul>

  <address class="address">
    421, Address line goes here<br>
    45452,Country Name
  </address>

  <div class="pattern-band" role="img" aria-label="Woven green stripe pattern along the bottom edge"></div>
</section>

<section class="card card--back">
  <div class="back-brand">
    <span class="brand__mark"></span>
    <p class="back-brand__name">Timber Ridge<br>Land Services</p>
  </div>
  <div class="pattern-band" role="img" aria-label="Woven green stripe pattern along the bottom edge"></div>
</section>

</body>
</html>
```